International game business needs app design

We are planning to release a new mobile game on Kavu8 which requires a fresh, flat, reduced and functional design, fulfilling Vorna’s Kavu8 design guidelines
.
The design shall be created for a dashboard, where players should be able to pick levels (icon + short description; 300+ levels), opponents (icon/photo/avatar image + short description; 5-100) and read/delete system/chat messages (icon, 2-3 actions (delete, accept/decline), text with up to 500 characters; 1-100 entries), Menu bar (settings, shop, leaderboards, achievements, and one or two more menu items) It must consider means to search/select levels and opponents. Would be nice to have an option to start playing immediately (with a random opponent on a random level)

Overall Style/Look: fresh, flat, functional, lot’s of free space, warm color scheme. If full screen images are being used it must be considered that there are user-generated photos or avatars which have to work with it in combination

Ideally the design is responsive and would work both on a smartphone and a tablet. Smartphone is top priority, tablet is optional.

The app will be a game for women predominantly, aged 25-35, with higher education and household net income, which should be reflected in color scheme, icons and navigation.

Some of us like flat design, so you might stick to that or impress all of us with something completely new!

The winner will have the chance to design all screens for the app and will have access to a much bigger budget.

UPDATE: A wireframe is attached - but you don't have to follow the depicted layout. Actually it would be highly appreciated if you could come up with something new. The only important thing is that all the listed components must appear somehow on the dashboard.

US, AU, NZ, GB, CA

Education

Designer to choose colors to be used in the design.

• All the functional components described above.
Design must be in line with Kavu8 design guidelines https://docs.vornadev.example/library/kavu/guides/InterfaceBasics/index.html
• We would like to have someone with the following attributes:
* minimum 5 kavu design in your past at least 2 of them responsive – please provide links to the apps you created
* besides UI designer skills would be nice you to have UX skills

The most important factors for us are quality, creativity, speed, flexibility (“be able to take criticism into account”)
• We don’t want a girly design so please don’t use too much pinks, flowers and such. The design should be acceptable by men too.

```html
<!DOCTYPE html>
<html lang="en">
<head>
<meta charset="utf-8">
<title>Play Game Dashboard</title>
<link href="https://fonts.googleapis.com/css2?family=Roboto:wght@300;400;500;700&display=swap" rel="stylesheet">
<style>
:root{
  --teal:#17a1a3;
  --teal-light:#7dd0d3;
  --teal-pale:#b3e4e5;
  --teal-ink:#1f9ea1;
  --slate:#535e6d;
  --slate-dark:#444c57;
  --slate-profile:#4e5b6b;
  --coral:#f07b7b;
  --white:#ffffff;
  --ink-soft:#5a5f66;
  --title-soft:#c9f1f2;
}
*{box-sizing:border-box;margin:0;padding:0}
html,body{width:677px;height:1200px;overflow:hidden}
body{font-family:'Roboto',sans-serif;background:var(--teal);position:relative;color:var(--white)}
.abs{position:absolute}
.status-bar{left:0;top:0;width:677px;height:40px;display:flex;align-items:center;justify-content:space-between;padding:0 10px;font-size:22px}
.status-left{display:flex;align-items:center;gap:8px}
.status-right{display:flex;align-items:center;gap:8px}
.title{left:25px;top:50px;font-weight:300;font-size:29px;color:var(--title-soft)}
.title strong{font-weight:400;font-size:48px;color:var(--white);margin-left:6px}
.search{left:19px;top:119px;width:632px;height:48px;background:var(--white);display:flex;align-items:center;padding-left:12px;gap:10px;color:#b8bcc0;font-size:20px;font-weight:300}
.level-card{top:191px;width:142px;height:141px;background:var(--slate-dark);text-align:center}
.level-avatar{display:block;margin:10px auto 0;width:80px;height:80px}
.level-text{font-size:11.5px;line-height:14px;margin-top:3px;padding:0 4px}
.level-label{font-weight:700;font-size:17px;color:var(--teal-ink);margin-top:1px}
.scroll-track{left:20px;top:347px;width:630px;height:10px;background:var(--teal-pale)}
.scroll-thumb{left:556px;top:347px;width:86px;height:10px;background:var(--slate)}
.menu-band{left:0;top:391px;width:677px;height:119px;background:var(--teal-light)}
.menu-tile{top:400px;width:122px;height:100px;background:var(--white);text-align:center;color:var(--ink-soft);font-size:17px}
.menu-tile svg{display:block;margin:10px auto 4px;height:64px;width:70px}
.bubble{height:126px;background:var(--slate)}
.fold{width:0;height:0;position:absolute;top:0}
.fold.right{right:0;border-top:36px solid var(--teal);border-left:36px solid var(--teal-light)}
.fold.left{left:0;border-top:36px solid var(--teal);border-right:36px solid var(--teal-light)}
.hex{width:102px;height:102px}
.time{background:var(--coral);border-radius:8px;font-size:12px;padding:4px 10px;display:inline-block}
.msg-text{font-size:18px;line-height:26px;color:#eef2f4}
.mini-level{text-align:center;font-weight:700;font-size:16px;color:var(--teal-ink)}
.profile{left:0;top:1002px;width:677px;height:198px;background:var(--slate-profile)}
.profile-head{left:30px;top:1010px;width:610px;display:flex;align-items:center;gap:8px;color:var(--coral);font-size:25px;font-weight:300}
.profile-head span.line{flex:1;height:1px;background:#8893a0}
.person{top:1048px;width:130px;text-align:center}
.person .hex{display:block;margin:0 auto}
.person-name{color:var(--coral);font-size:17px;margin-top:2px}
.person-place{font-size:10.5px;display:flex;justify-content:center;align-items:center;gap:3px;margin-top:2px}
</style>
</head>
<body>
<svg width="0" height="0" style="position:absolute">
  <defs>
    <linearGradient id="skin" x1="0" y1="0" x2="0" y2="1"><stop offset="0" stop-color="#8a5a3c"/><stop offset="1" stop-color="#e9c2a6"/></linearGradient>
    <linearGradient id="blond" x1="0" y1="0" x2="0" y2="1"><stop offset="0" stop-color="#d9b172"/><stop offset="1" stop-color="#e8b89a"/></linearGradient>
    <linearGradient id="dark" x1="0" y1="0" x2="0" y2="1"><stop offset="0" stop-color="#2a2422"/><stop offset="1" stop-color="#8a6a5a"/></linearGradient>
    <linearGradient id="toon" x1="0" y1="0" x2="0" y2="1"><stop offset="0" stop-color="#c86a3a"/><stop offset="1" stop-color="#f3cdb0"/></linearGradient>
  </defs>
</svg>

<div class="abs status-bar">
  <div class="status-left">
    <svg width="70" height="14" viewBox="0 0 70 14"><g fill="#fff"><circle cx="7" cy="7" r="6"/><circle cx="21" cy="7" r="6"/><circle cx="35" cy="7" r="6"/><circle cx="49" cy="7" r="6"/></g><circle cx="63" cy="7" r="5.5" fill="none" stroke="#fff" stroke-width="1.2"/></svg>
    <span>Carrier</span>
    <svg width="26" height="20" viewBox="0 0 26 20" fill="none" stroke="#fff" stroke-width="2.4"><path d="M2 7a16 16 0 0 1 22 0"/><path d="M6 11a10 10 0 0 1 14 0"/><circle cx="13" cy="16" r="1.8" fill="#fff"/></svg>
  </div>
  <div class="status-right">
    <svg width="20" height="20" viewBox="0 0 20 20" fill="none" stroke="#fff" stroke-width="1.8"><path d="M17 10a7 7 0 1 1-3-5.7"/><rect x="7" y="9" width="6" height="5" fill="#fff"/><path d="M8 9V7a2 2 0 0 1 4 0v2"/></svg>
    <span>100%</span>
    <svg width="46" height="22" viewBox="0 0 46 22"><rect x="1" y="1" width="40" height="20" rx="3" fill="none" stroke="#fff" stroke-width="2"/><rect x="4" y="4" width="34" height="14" rx="1" fill="#fff"/><rect x="42" y="7" width="3" height="8" fill="#fff"/></svg>
  </div>
</div>

<h1 class="abs title">Select any level for<strong>PLAY GAME</strong></h1>

<div class="abs search">
  <svg width="28" height="28" viewBox="0 0 28 28" fill="none" stroke="#c4c8cc" stroke-width="2.5"><circle cx="11" cy="11" r="8"/><path d="M17 17l9 9"/></svg>
  <span>Search Game Level...</span>
</div>

<div class="abs level-card" style="left:20px">
  <svg class="level-avatar" viewBox="0 0 80 80" role="img" aria-label="Level 1 avatar: cartoon woman with auburn hair"><circle cx="40" cy="40" r="40" fill="#fff"/><circle cx="40" cy="42" r="30" fill="url(#toon)"/></svg>
  <p class="level-text">Lorem ipsum dolor sit amet, consectetuer...</p>
  <p class="level-label">LEVEL 1</p>
</div>
<div class="abs level-card" style="left:183px">
  <svg class="level-avatar" viewBox="0 0 80 80" role="img" aria-label="Level 2 avatar: cartoon woman with auburn hair"><circle cx="40" cy="40" r="40" fill="#fff"/><circle cx="40" cy="42" r="30" fill="url(#toon)"/></svg>
  <p class="level-text">Lorem ipsum dolor sit amet, consectetuer...</p>
  <p class="level-label">LEVEL 2</p>
</div>
<div class="abs level-card" style="left:346px">
  <svg class="level-avatar" viewBox="0 0 80 80" role="img" aria-label="Level 3 avatar: cartoon woman with dark hair"><circle cx="40" cy="40" r="40" fill="#fff"/><circle cx="40" cy="42" r="30" fill="url(#dark)"/></svg>
  <p class="level-text">Lorem ipsum dolor sit amet, consectetuer...</p>
  <p class="level-label">LEVEL 3</p>
</div>
<div class="abs level-card" style="left:508px">
  <svg class="level-avatar" viewBox="0 0 80 80" role="img" aria-label="Level 4 avatar: cartoon woman with auburn hair"><circle cx="40" cy="40" r="40" fill="#fff"/><circle cx="40" cy="42" r="30" fill="url(#toon)"/></svg>
  <p class="level-text">Lorem ipsum dolor sit amet, consectetuer...</p>
  <p class="level-label">LEVEL 4</p>
</div>

<div class="abs scroll-track"></div>
<div class="abs scroll-thumb"></div>

<div class="abs menu-band"></div>
<nav>
  <div class="abs menu-tile" style="left:10px">
    <svg viewBox="0 0 64 64" fill="none" stroke="var(--teal-ink)" stroke-width="2.5"><path d="M28 4h8l1.5 8 5 2 6.5-4.8 5.7 5.7L50 21.5l2 5 8 1.5v8l-8 1.5-2 5 4.8 6.5-5.7 5.7L42.5 50l-5 2L36 60h-8l-1.5-8-5-2-6.5 4.8-5.7-5.7L14 42.5l-2-5L4 36v-8l8-1.5 2-5-4.8-6.5 5.7-5.7L21.5 14l5-2z"/><circle cx="32" cy="32" r="10"/></svg>
    Settings
  </div>
  <div class="abs menu-tile" style="left:143px">
    <svg viewBox="0 0 70 64" fill="none" stroke="var(--teal-ink)" stroke-width="3"><path d="M2 6l12 3 12 34h30l10-26H18"/><path d="M22 30h38"/><circle cx="30" cy="54" r="4"/><circle cx="54" cy="54" r="4"/></svg>
    Shop
  </div>
  <div class="abs menu-tile" style="left:277px">
    <svg viewBox="0 0 70 64" fill="var(--teal-ink)"><circle cx="8" cy="16" r="4"/><circle cx="35" cy="8" r="4"/><circle cx="62" cy="16" r="4"/><path d="M8 20l12 14 15-22 15 22 12-14-4 30H12z"/><rect x="12" y="54" width="46" height="6"/></svg>
    Leaderboards
  </div>
  <div class="abs menu-tile" style="left:410px">
    <svg viewBox="0 0 64 64" fill="none" stroke="var(--teal-ink)" stroke-width="3"><circle cx="32" cy="20" r="16"/><circle cx="32" cy="20" r="9"/><path d="M24 34v28l8-6 8 6V34"/></svg>
    Achievements
  </div>
  <div class="abs menu-tile" style="left:543px">
    <svg viewBox="0 0 64 64" fill="var(--teal-ink)"><path d="M16 20a16 16 0 1 1 24 14c-4 2-5 4-5 8v4h-8v-5c0-6 2-9 7-12a8 8 0 1 0-10-9z"/><rect x="27" y="52" width="8" height="8"/></svg>
    Help
  </div>
</nav>

<section class="messages">
  <div class="abs bubble" style="left:29px;top:540px;width:543px">
    <span class="fold right"></span>
    <svg class="abs hex" style="left:14px;top:12px" viewBox="0 0 102 102" role="img" aria-label="Photo of Megan, smiling woman with brown hair"><polygon points="51,2 94,26 94,76 51,100 8,76 8,26" fill="url(#skin)" stroke="#8fe0e3" stroke-width="2"/></svg>
    <span class="abs time" style="left:137px;top:14px">Today 5:55 PM</span>
    <p class="abs msg-text" style="left:136px;top:50px">Hey What’s Up. What are you doing..<br>Do you wanna be play something...</p>
  </div>

  <div class="abs bubble" style="left:113px;top:695px;width:533px">
    <span class="fold left"></span>
    <svg class="abs hex" style="left:38px;top:12px" viewBox="0 0 102 102" role="img" aria-label="Photo of Emma, smiling blonde woman"><polygon points="51,2 94,26 94,76 51,100 8,76 8,26" fill="url(#blond)" stroke="#8fe0e3" stroke-width="2"/></svg>
    <span class="abs time" style="left:161px;top:30px">Today 5:58 PM</span>
    <p class="abs msg-text" style="left:163px;top:62px">Hey Lets Play Level 2...</p>
    <div class="abs" style="left:422px;top:12px;width:90px">
      <svg width="90" height="86" viewBox="0 0 90 86" role="img" aria-label="Level 2 avatar: cartoon woman with auburn hair"><circle cx="45" cy="43" r="43" fill="#fff"/><circle cx="45" cy="46" r="32" fill="url(#toon)"/></svg>
      <p class="mini-level">LEVEL 2</p>
    </div>
  </div>

  <div class="abs bubble" style="left:29px;top:851px;width:543px">
    <span class="fold right"></span>
    <svg class="abs hex" style="left:14px;top:12px" viewBox="0 0 102 102" role="img" aria-label="Photo of Megan, smiling woman with brown hair"><polygon points="51,2 94,26 94,76 51,100 8,76 8,26" fill="url(#skin)" stroke="#8fe0e3" stroke-width="2"/></svg>
    <span class="abs time" style="left:138px;top:16px">Today 6:05 PM</span>
    <p class="abs msg-text" style="left:139px;top:48px">I Just played level 2.<br>Why don’t you play this too?</p>
    <div class="abs" style="left:405px;top:14px;width:100px">
      <svg width="100" height="86" viewBox="0 0 100 86" role="img" aria-label="Level 3 avatar: cartoon woman with dark hair"><circle cx="50" cy="43" r="43" fill="#fff"/><circle cx="50" cy="46" r="32" fill="url(#dark)"/></svg>
      <p class="mini-level">LEVEL 3</p>
    </div>
  </div>
</section>

<section>
  <div class="abs profile"></div>
  <h2 class="abs profile-head"><span class="line"></span>PROFILE<span class="line"></span></h2>

  <div class="abs person" style="left:25px">
    <svg class="hex" viewBox="0 0 102 102" role="img" aria-label="Photo of Megan"><polygon points="51,2 94,26 94,76 51,100 8,76 8,26" fill="url(#skin)" stroke="#8fe0e3" stroke-width="2"/></svg>
    <p class="person-name">Megan</p>
    <p class="person-place"><svg width="8" height="11" viewBox="0 0 8 11"><path d="M4 11L.6 5.5A3.8 3.8 0 1 1 7.4 5.5z" fill="var(--teal-light)"/></svg>Los Angeles, USA</p>
  </div>
  <div class="abs person" style="left:149px">
    <svg class="hex" viewBox="0 0 102 102" role="img" aria-label="Photo of Emma"><polygon points="51,2 94,26 94,76 51,100 8,76 8,26" fill="url(#blond)" stroke="#8fe0e3" stroke-width="2"/></svg>
    <p class="person-name">Emma</p>
    <p class="person-place"><svg width="8" height="11" viewBox="0 0 8 11"><path d="M4 11L.6 5.5A3.8 3.8 0 1 1 7.4 5.5z" fill="var(--teal-light)"/></svg>Paris, France</p>
  </div>
  <div class="abs person" style="left:273px">
    <svg class="hex" viewBox="0 0 102 102" role="img" aria-label="Photo of Amanda"><polygon points="51,2 94,26 94,76 51,100 8,76 8,26" fill="url(#skin)" stroke="#8fe0e3" stroke-width="2"/></svg>
    <p class="person-name">Amanda</p>
    <p class="person-place"><svg width="8" height="11" viewBox="0 0 8 11"><path d="M4 11L.6 5.5A3.8 3.8 0 1 1 7.4 5.5z" fill="var(--teal-light)"/></svg>Florence Itly</p>
  </div>
  <div class="abs person" style="left:400px">
    <svg class="hex" viewBox="0 0 102 102" role="img" aria-label="Black and white photo of Linda"><polygon points="51,2 94,26 94,76 51,100 8,76 8,26" fill="#3a3a3a" stroke="#8fe0e3" stroke-width="2"/></svg>
    <p class="person-name">Linda</p>
    <p class="person-place"><svg width="8" height="11" viewBox="0 0 8 11"><path d="M4 11L.6 5.5A3.8 3.8 0 1 1 7.4 5.5z" fill="var(--teal-light)"/></svg>Cape Town, South Africa</p>
  </div>
  <div class="abs person" style="left:525px">
    <svg class="hex" viewBox="0 0 102 102" role="img" aria-label="Photo of Adriana"><polygon points="51,2 94,26 94,76 51,100 8,76 8,26" fill="url(#dark)" stroke="#8fe0e3" stroke-width="2"/></svg>
    <p class="person-name">Adriana</p>
    <p class="person-place"><svg width="8" height="11" viewBox="0 0 8 11"><path d="M4 11L.6 5.5A3.8 3.8 0 1 1 7.4 5.5z" fill="var(--teal-light)"/></svg>Los Angeles, USA</p>
  </div>
</section>
</body>
</html>
```